Varno Building Pty Ltd need an Identity!

We need a logo design for a building company based in Sydney, Australia. In addition - Business Card Layout. The colour scheme is to be black and red and communicate a professional yet 'hands on' approach to building.

Target Market(s)

Architects, Home Owners, Developers

Industry/Entity Type

Construction

Font styles to use
Serif
Sans Serif

Colors
ec1f27

Requirements
Must have
• Clear logo and professional direction.
Nice to have
• Use of initials as a possible logo
Should not have
• Graphics/pictures of houses, house roofs etc. Can be an abstracted form of a building.

```html
<!DOCTYPE html>
<html lang="en">
<head>
<meta charset="utf-8">
<title>Varno Building Pty Ltd – Identity</title>
<link href="https://fonts.googleapis.com/css2?family=Lato:wght@400;700&display=swap" rel="stylesheet">
<style>
  :root{
    --red:#ec1f27;
    --black:#282526;
    --ink:#4a4a4a;
    --paper:#ffffff;
    --canvas:#ededed;
    --rule:#8a8a8a;
  }
  *{box-sizing:border-box;margin:0;padding:0}
  html,body{width:1200px;height:1200px;overflow:hidden}
  body{background:var(--canvas);font-family:'Lato',sans-serif;position:relative;color:var(--ink)}

  .card{position:absolute;width:600px;height:343px;box-shadow:0 8px 22px rgba(0,0,0,.12)}
  .card--back{left:540px;top:110px;background:var(--black);display:flex;align-items:center;justify-content:center}
  .card--front{left:60px;top:440px;background:var(--paper)}

  .wordmark{display:flex;align-items:center;gap:12px;text-transform:uppercase;letter-spacing:.04em;font-weight:400}
  .wordmark__square{background:var(--red);flex:none}
  .card--back .wordmark{color:#e6e6e6;font-size:19px}
  .card--back .wordmark__square{width:34px;height:34px}

  .front__brand{position:absolute;left:40px;top:34px;color:var(--ink);font-size:15px}
  .front__brand .wordmark__square{width:28px;height:28px}
  .front__rule{position:absolute;left:40px;right:40px;top:90px;height:1px;background:var(--rule)}

  .contacts{position:absolute;left:40px;top:108px;list-style:none;font-size:14px;line-height:23px}
  .contacts li{display:flex;align-items:center;gap:10px}
  .contacts svg{width:12px;height:12px;flex:none}

  .person{position:absolute;right:40px;bottom:74px;text-align:right;width:230px}
  .person__name{color:var(--red);font-weight:700;font-size:17px}
  .person__title{font-size:14px;margin-top:1px}
  .person__rule{height:1px;background:var(--rule);margin:8px 0 8px}
  .person__address{font-size:14px;line-height:19px;display:flex;justify-content:flex-end;gap:10px;align-items:flex-start}
  .person__address svg{width:11px;height:14px;margin-top:3px;flex:none}

  .card__edge{position:absolute;left:0;right:0;bottom:0}
  .card__edge-red{height:2px;background:var(--red);margin-bottom:6px}
  .card__edge-black{height:14px;background:var(--black)}

  .lockup{position:absolute;left:110px;top:960px;flex-direction:column;align-items:flex-start;gap:22px}
  .lockup .wordmark__square{width:90px;height:90px;margin-left:120px}
  .lockup__name{font-size:26px;color:var(--black);letter-spacing:.02em}
</style>
</head>
<body>

  <section class="card card--back" aria-label="Business card back">
    <div class="wordmark">
      <span class="wordmark__square"></span>
      <span>Varno Building Pty Ltd</span>
    </div>
  </section>

  <section class="card card--front" aria-label="Business card front">
    <div class="wordmark front__brand">
      <span class="wordmark__square"></span>
      <span>Varno Building Pty Ltd</span>
    </div>
    <div class="front__rule"></div>

    <ul class="contacts">
      <li>
        <svg viewBox="0 0 12 12"><path d="M2.5 1l2 2-1 1.5c.6 1.4 1.6 2.4 3 3L8 6.5l2 2-1.3 1.8C5 10 2 7 1.7 3.3z" fill="none" stroke="var(--red)" stroke-width="1.1"/></svg>
        02.9410.3368
      </li>
      <li>
        <svg viewBox="0 0 12 12"><rect x="1" y="4" width="10" height="5" fill="none" stroke="var(--red)" stroke-width="1.1"/><rect x="3" y="1" width="6" height="3" fill="none" stroke="var(--red)" stroke-width="1.1"/><rect x="3" y="7" width="6" height="4" fill="#fff" stroke="var(--red)" stroke-width="1.1"/></svg>
        02.9410.3369
      </li>
      <li>
        <svg viewBox="0 0 12 12"><rect x="1" y="2.5" width="10" height="7" fill="none" stroke="var(--red)" stroke-width="1.1"/><path d="M1 2.5l5 4 5-4" fill="none" stroke="var(--red)" stroke-width="1.1"/></svg>
        liam@varnobuilding.com
      </li>
      <li>
        <svg viewBox="0 0 12 12"><rect x="1" y="1.5" width="10" height="7.5" fill="none" stroke="var(--red)" stroke-width="1.1"/><path d="M4 11h4M6 9v2" stroke="var(--red)" stroke-width="1.1"/></svg>
        www.varnobuilding.com
      </li>
    </ul>

    <div class="person">
      <div class="person__name">Liam Carter</div>
      <div class="person__title">director</div>
      <div class="person__rule"></div>
      <div class="person__address">
        <span>18 Harbour Lane<br>Parramatta NSW 2150</span>
        <svg viewBox="0 0 11 14"><path d="M5.5 13S1 8 1 5a4.5 4.5 0 0 1 9 0c0 3-4.5 8-4.5 8z" fill="none" stroke="var(--red)" stroke-width="1.1"/><circle cx="5.5" cy="5" r="1.5" fill="var(--red)"/></svg>
      </div>
    </div>

    <div class="card__edge">
      <div class="card__edge-red"></div>
      <div class="card__edge-black"></div>
    </div>
  </section>

  <div class="wordmark lockup">
    <span class="wordmark__square"></span>
    <span class="lockup__name">Varno Building Pty Ltd</span>
  </div>

</body>
</html>
```